Construction APP

We need to design a modern app IOS/Android where my team can create a profile with their info, (maybe share some pictures), reviews, submit time cards, show their availability, etc.

Like a taxi app but for construction. We also want to be able to assign each team member to a project manager with who they currently working. So we will also need to be able to create profiles at the Administration level.

The goal is to keep innovating the app as we grow, so we are always open to suggestions and ideas.

Industry/Entity Type

Construction

Colors
FFC000
F8CF3A
FAE287
FDF2CF
FEFAEE

Requirements
Must have
• IOS/Android APP where my team can create a profile with their info, (maybe share some pictures), reviews, submit time cards, show their availability, etc.We also want to be able to assign each team member to a project manager with who they currently working. So we will also need to be able to create profiles at the Administration level.

```html
<!DOCTYPE html>
<html lang="en">
<head>
<meta charset="utf-8">
<title>Stonefield Crew – App Screens</title>
<link href="https://fonts.googleapis.com/css2?family=Open+Sans:wght@400;600;700&display=swap" rel="stylesheet">
<style>
  :root {
    --amber: #FFC000;
    --yellow: #F8CF3A;
    --butter: #FAE287;
    --cream: #FDF2CF;
    --ivory: #FEFAEE;
    --panel: #F5EFDC;
    --ink: #111111;
    --text: #333333;
    --muted: #666666;
    --star: #F7A600;
    --photo-warm: #E8962A;
    --photo-deep: #C9701E;
  }
  * { box-sizing: border-box; margin: 0; padding: 0; }
  html, body { width: 1200px; height: 857px; overflow: hidden; }
  body {
    background: var(--yellow);
    font-family: "Open Sans", Arial, sans-serif;
    color: var(--text);
    position: relative;
  }
  .screen {
    position: absolute; top: 81px; width: 316px; height: 682px;
    border-radius: 30px; overflow: hidden; background: #fff;
  }
  .screen--welcome { left: 45px; background: linear-gradient(180deg, #FBE38E 0%, var(--butter) 60%); }
  .screen--profile { left: 441px; background: var(--panel); }
  .screen--reviews { left: 836px; }
  .status { position: absolute; top: 14px; left: 0; right: 0; height: 16px; z-index: 3;
    display: flex; justify-content: space-between; padding: 0 22px 0 32px;
    color: #fff; font-size: 12px; font-weight: 600; }
  .status svg { display: block; }
  /* welcome */
  .brand { position: absolute; top: 170px; left: 0; right: 0; display: flex;
    align-items: center; justify-content: center; gap: 10px; }
  .brand__dot { width: 22px; height: 22px; border-radius: 50%; background: var(--ink); }
  .brand__name { font-size: 28px; font-weight: 700; color: var(--ink); letter-spacing: 0.5px; }
  .dome { position: absolute; left: -60px; right: -60px; top: 321px; height: 600px;
    background: var(--ink); border-radius: 50% 50% 0 0 / 110px 110px 0 0; }
  .btn { position: absolute; left: 54px; width: 207px; height: 50px; border-radius: 8px;
    display: flex; align-items: center; justify-content: center;
    font-size: 18px; font-weight: 700; }
  .btn--fill { background: var(--yellow); color: var(--ink); }
  .btn--outline { border: 2px solid var(--yellow); color: var(--yellow); }
  /* profile */
  .cover { position: absolute; left: 0; top: 0; width: 100%;
    background: linear-gradient(135deg, var(--photo-deep) 0%, var(--photo-warm) 45%, #F0D36A 100%); }
  .back { position: absolute; top: 66px; left: 34px; z-index: 3; }
  .profile-head { position: absolute; top: 138px; left: 0; right: 0; height: 132px; background: #fff; text-align: center; }
  .avatar-square { position: absolute; top: 85px; left: 112px; width: 92px; height: 94px;
    border: 3px solid #fff; border-radius: 4px; z-index: 2;
    background: linear-gradient(180deg, #9BA7AE, #5E6A72); }
  .profile-head__name { margin-top: 52px; font-size: 19px; font-weight: 600; color: #444; }
  .profile-head__role { margin-top: 4px; font-size: 14px; color: #444; }
  .stars { display: flex; gap: 3px; justify-content: center; margin-top: 6px; }
  .card { position: absolute; left: 5px; width: 306px; background: #fff; border-radius: 6px; padding: 16px 13px; }
  .card__title { font-size: 14px; color: var(--text); letter-spacing: 0.3px; }
  .card__body { font-size: 14px; color: var(--muted); line-height: 24px; margin-top: 4px; }
  .card__link { font-size: 12px; font-weight: 600; color: var(--amber); text-decoration: underline; margin-top: 3px; display: block; }
  .phone-line { display: flex; align-items: center; gap: 8px; }
  /* reviews */
  .tab { position: absolute; top: 100px; left: 80px; width: 158px; height: 60px; background: #fff;
    border-radius: 8px 8px 0 0; text-align: center; padding-top: 18px; font-size: 16px; color: var(--ink); z-index: 2; }
  .tab::after { content: ""; display: block; width: 30px; height: 3px; background: var(--yellow); margin: 6px auto 0; }
  .summary { position: absolute; top: 162px; left: 4px; }
  .summary__score { font-size: 26px; font-weight: 700; color: var(--ink); line-height: 1; }
  .summary__users { font-size: 12px; color: var(--text); margin-top: 4px; display: flex; align-items: center; gap: 4px; }
  .summary .stars { justify-content: flex-start; margin-top: 3px; gap: 1px; }
  .ring { position: absolute; top: 165px; right: 4px; width: 58px; height: 58px; }
  .ring__label { position: absolute; inset: 0; text-align: center; padding-top: 15px; font-size: 13px; font-weight: 600; color: #444; line-height: 1; }
  .ring__label small { display: block; font-size: 7px; font-weight: 400; margin-top: 2px; }
  .review { position: absolute; left: 4px; width: 310px; height: 118px; background: var(--ivory); border-radius: 6px; padding: 14px 12px 0 70px; }
  .review__avatar { position: absolute; left: 10px; top: 12px; width: 42px; height: 42px; border-radius: 50%; }
  .review__name { font-size: 13px; color: var(--ink); }
  .review__time { font-size: 8px; color: var(--muted); }
  .review__text { font-size: 12.5px; color: var(--muted); line-height: 19px; margin-top: 6px; }
  .review .stars { position: absolute; right: 12px; top: 16px; gap: 1px; margin: 0; }
  .more { position: absolute; left: 151px; top: 643px; }
</style>
</head>
<body>
<svg width="0" height="0" style="position:absolute">
  <defs>
    <symbol id="star" viewBox="0 0 20 20"><path d="M10 1l2.6 6 6.4.5-4.9 4.2 1.5 6.3L10 14.7 4.4 18l1.5-6.3L1 7.5l6.4-.5z" fill="#F7A600"/></symbol>
    <symbol id="status-icons" viewBox="0 0 60 12">
      <rect x="0" y="8" width="2" height="3" fill="currentColor"/><rect x="3" y="6" width="2" height="5" fill="currentColor"/>
      <rect x="6" y="4" width="2" height="7" fill="currentColor"/><rect x="9" y="2" width="2" height="9" fill="currentColor"/>
      <path d="M18 5a9 9 0 0 1 12 0l-1.5 1.5a7 7 0 0 0-9 0zM21 8a5 5 0 0 1 6 0L24 11z" fill="currentColor"/>
      <rect x="36" y="2" width="20" height="9" rx="2" fill="none" stroke="currentColor"/><rect x="38" y="4" width="16" height="5" fill="currentColor"/>
    </symbol>
  </defs>
</svg>

<section class="screen screen--welcome">
  <div class="status"><span>9:30</span><svg width="48" height="12" style="color:#fff"><use href="#status-icons"/></svg></div>
  <div class="brand"><span class="brand__dot"></span><span class="brand__name">STONEFIELD CREW</span></div>
  <div class="dome" role="img" aria-label="Dark blueprint background"></div>
  <div class="btn btn--fill" style="top:405px">Register</div>
  <div class="btn btn--outline" style="top:465px">Login</div>
</section>

<section class="screen screen--profile">
  <div class="cover" style="height:138px" role="img" aria-label="Photo of construction tools on a workbench"></div>
  <div class="status"><span>9:30</span><svg width="48" height="12" style="color:#fff"><use href="#status-icons"/></svg></div>
  <svg class="back" width="22" height="12" viewBox="0 0 22 12"><path d="M21 6H2M7 1L2 6l5 5" stroke="#fff" stroke-width="1.6" fill="none"/></svg>
  <div class="avatar-square" role="img" aria-label="Profile photo of a worker in a hard hat"></div>
  <div class="profile-head">
    <p class="profile-head__name">Lorem Ipsum</p>
    <p class="profile-head__role">Sed ut perspiciatis unde omnis</p>
    <div class="stars"><svg width="15" height="15"><use href="#star"/></svg><svg width="15" height="15"><use href="#star"/></svg><svg width="15" height="15"><use href="#star"/></svg><svg width="15" height="15"><use href="#star"/></svg><svg width="15" height="15"><use href="#star"/></svg></div>
  </div>
  <div class="card" style="top:281px;height:120px">
    <p class="card__title">ABOUT</p>
    <p class="card__body">Lorem ipsum dolor sit amet, consectetur adipiscing elit, sed do eiusmod tempor.</p>
    <span class="card__link">READ MORE</span>
  </div>
  <div class="card" style="top:412px;height:164px;padding-left:18px">
    <p class="card__title" style="margin-top:6px">AVAILABILITY</p>
    <p class="card__body" style="margin-top:6px">Mon - Fri: 9:00 - 20:00<br>Sat - Sun: 11:00 - 22:00</p>
    <p class="card__title" style="margin-top:12px">PHONE NUMBER</p>
    <p class="card__body phone-line" style="margin-top:6px"><svg width="13" height="13" viewBox="0 0 24 24"><path d="M6.6 10.8a15 15 0 0 0 6.6 6.6l2.2-2.2c.3-.3.7-.4 1-.2 1.1.4 2.3.6 3.6.6.6 0 1 .4 1 1V20c0 .6-.4 1-1 1A17 17 0 0 1 3 4c0-.6.4-1 1-1h3.5c.6 0 1 .4 1 1 0 1.3.2 2.5.6 3.6.1.3 0 .7-.2 1z" fill="#555"/></svg>555-014-2290</p>
  </div>
  <div class="btn btn--fill" style="top:588px;left:55px">submit time cards</div>
</section>

<section class="screen screen--reviews">
  <div class="cover" style="height:150px" role="img" aria-label="Photo of construction tools on a workbench"></div>
  <div class="status"><span>9:30</span><svg width="48" height="12" style="color:#fff"><use href="#status-icons"/></svg></div>
  <svg class="back" width="22" height="12" viewBox="0 0 22 12"><path d="M21 6H2M7 1L2 6l5 5" stroke="#fff" stroke-width="1.6" fill="none"/></svg>
  <div class="tab">REVIEWS</div>
  <div class="summary">
    <p class="summary__score">4.5</p>
    <p class="summary__users"><svg width="9" height="9" viewBox="0 0 10 10"><circle cx="5" cy="3" r="2.3" fill="#555"/><path d="M0.5 10a4.5 4 0 0 1 9 0z" fill="#555"/></svg>120 total users</p>
    <div class="stars"><svg width="11" height="11"><use href="#star"/></svg><svg width="11" height="11"><use href="#star"/></svg><svg width="11" height="11"><use href="#star"/></svg><svg width="11" height="11"><use href="#star"/></svg><svg width="11" height="11"><use href="#star"/></svg></div>
  </div>
  <div class="ring">
    <svg width="58" height="58" viewBox="0 0 58 58"><circle cx="29" cy="29" r="26" fill="none" stroke="#E2E2E2" stroke-width="4"/><circle cx="29" cy="29" r="26" fill="none" stroke="#F8CF3A" stroke-width="4" stroke-dasharray="139 163" transform="rotate(-30 29 29)"/></svg>
    <p class="ring__label">85<small>Total users</small></p>
  </div>

  <article class="review" style="top:251px">
    <div class="review__avatar" role="img" aria-label="Reviewer photo" style="background:var(--amber)"></div>
    <p class="review__name">Lorem Ipsum</p><p class="review__time">2 Months ago</p>
    <div class="stars"><svg width="11" height="11"><use href="#star"/></svg><svg width="11" height="11"><use href="#star"/></svg><svg width="11" height="11"><use href="#star"/></svg><svg width="11" height="11"><use href="#star"/></svg><svg width="11" height="11"><use href="#star"/></svg></div>
    <p class="review__text">Ut enim ad minima veniam, quis nostrum exercitationem ullam corporis suscipit laboriosam.</p>
  </article>
  <article class="review" style="top:380px">
    <div class="review__avatar" role="img" aria-label="Reviewer photo" style="background:#B8A48E"></div>
    <p class="review__name">Lorem Ipsum</p><p class="review__time">2 Months ago</p>
    <div class="stars"><svg width="11" height="11"><use href="#star"/></svg><svg width="11" height="11"><use href="#star"/></svg><svg width="11" height="11"><use href="#star"/></svg><svg width="11" height="11"><use href="#star"/></svg><svg width="11" height="11"><use href="#star"/></svg></div>
    <p class="review__text">Ut enim ad minima veniam, quis nostrum exercitationem ullam corporis suscipit laboriosam.</p>
  </article>
  <article class="review" style="top:509px">
    <div class="review__avatar" role="img" aria-label="Reviewer photo" style="background:#9FB3C2"></div>
    <p class="review__name">Lorem Ipsum</p><p class="review__time">2 Months ago</p>
    <div class="stars"><svg width="11" height="11"><use href="#star"/></svg><svg width="11" height="11"><use href="#star"/></svg><svg width="11" height="11"><use href="#star"/></svg><svg width="11" height="11"><use href="#star"/></svg><svg width="11" height="11"><use href="#star"/></svg></div>
    <p class="review__text">Ut enim ad minima veniam, quis nostrum exercitationem ullam corporis suscipit laboriosam.</p>
  </article>
  <svg class="more" width="14" height="14" viewBox="0 0 14 14"><circle cx="7" cy="7" r="7" fill="#F7A600"/><path d="M4 4.5l3 2.5 3-2.5M4 7.5l3 2.5 3-2.5" stroke="#fff" stroke-width="1.3" fill="none"/></svg>
</section>
</body>
</html>
```